BHS business card

We have just had a new logo designed and I an struggling to put it together on the new stationary items. We just want something clean but eye catching. I want to stay with the colors that will go well with our logo.
We are a wildlife rescue that does wild and domestic birds only. So birds incorporated into the design would be fine as well
Updates
Thank you to everyone for your designs, we loved them all and had a very hard time choosing.
Industry/Entity Type
Business
Contact Information for Business Card
Briarwood Heron Sanctuary
P.O. Box 2736
8127 Tanager Road
Indian Trail, NC 28412
www.bhsanctum.org
704-555-2317
helpline@bhsanctum.org
Look and feel
Each slider illustrates characteristics of the customer's brand and the style your logo design should communicate.

```html
<!DOCTYPE html>
<html lang="en">
<head>
<meta charset="utf-8">
<title>BHS business card</title>
<link href="https://fonts.googleapis.com/css2?family=Exo+2:wght@400;500;600&display=swap" rel="stylesheet">
<style>
  :root {
    --stage: #e9eaec;
    --card: #ffffff;
    --blue: #2f6db5;
    --blue-deep: #1f58a3;
    --green: #7fbf3f;
    --green-light: #a6d35a;
    --ink: #3a3a3a;
    --ink-soft: #6a6a6a;
    --brand: #2e6cb0;
  }
  * { margin: 0; padding: 0; box-sizing: border-box; }
  html, body { width: 1200px; height: 901px; overflow: hidden; }
  body {
    background: var(--stage);
    font-family: "Exo 2", sans-serif;
    display: flex;
    align-items: center;
    justify-content: center;
    gap: 90px;
  }
  .card {
    position: relative;
    width: 300px;
    height: 520px;
    background: var(--card);
    border-radius: 26px;
    overflow: hidden;
    box-shadow: 0 10px 28px rgba(0,0,0,0.16);
  }
  .card-front .wave {
    position: absolute;
    left: 0; top: 0;
    width: 100%; height: 100%;
  }
  .holder {
    position: absolute;
    left: 28px; top: 34px;
    color: var(--ink);
  }
  .holder-name {
    font-size: 19px;
    font-weight: 500;
    letter-spacing: 2px;
    text-transform: uppercase;
  }
  .holder-role {
    margin-top: 4px;
    font-size: 12.5px;
    color: var(--ink-soft);
    letter-spacing: 0.5px;
  }
  .brand {
    position: absolute;
    display: flex;
    flex-direction: column;
    align-items: center;
    text-align: center;
    gap: 10px;
  }
  .brand-mark {
    width: 84px; height: 70px;
    background: var(--green-light);
    flex: none;
  }
  .brand-name {
    font-size: 13px;
    font-weight: 600;
    line-height: 1.25;
    color: var(--brand);
    text-transform: uppercase;
    letter-spacing: 1px;
  }
  .card-front .brand { left: 50%; top: 110px; transform: translateX(-50%); width: 200px; }
  .contact {
    position: absolute;
    right: 26px; bottom: 26px;
    list-style: none;
    color: #ffffff;
    font-size: 11.5px;
    line-height: 1.75;
    letter-spacing: 0.4px;
  }
  .contact li { display: flex; justify-content: flex-end; align-items: center; gap: 7px; }
  .contact svg { width: 10px; height: 10px; fill: #ffffff; flex: none; }
  .contact .spacer { width: 10px; flex: none; }
  .card-back .brand {
    left: 50%; top: 50%;
    transform: translate(-50%, -55%);
    width: 220px;
  }
  .card-back .brand-mark { width: 110px; height: 92px; }
  .card-back .brand-name { font-size: 15px; }
</style>
</head>
<body>
  <section class="card card-front" aria-label="Card front">
    <svg class="wave" viewBox="0 0 300 520" preserveAspectRatio="none" aria-hidden="true">
      <defs>
        <linearGradient id="blueFill" x1="0" y1="0" x2="1" y2="1">
          <stop offset="0" stop-color="#3a7cc4"/>
          <stop offset="1" stop-color="#1f58a3"/>
        </linearGradient>
      </defs>
      <path d="M0 250 C 70 300, 170 330, 300 336 L300 520 L0 520 Z" fill="var(--green)"/>
      <path d="M0 258 C 70 310, 170 342, 300 350 L300 520 L0 520 Z" fill="#ffffff"/>
      <path d="M0 264 C 70 318, 170 350, 300 358 L300 520 L0 520 Z" fill="url(#blueFill)"/>
    </svg>

    <div class="holder">
      <p class="holder-name">Daniel Whitmore</p>
      <p class="holder-role">Managing Director</p>
    </div>

    <div class="brand">
      <span class="brand-mark"></span>
      <span class="brand-name">Briarwood Heron<br>Sanctuary</span>
    </div>

    <ul class="contact">
      <li>P.O. Box 2736, 8127 Tanager Road<span class="spacer"></span></li>
      <li>Indian Trail, NC 28412<span class="spacer"></span></li>
      <li>704-555-2317
        <svg viewBox="0 0 10 10"><path d="M2 0.5 L3.6 0.5 L4.3 2.8 L3.2 3.7 C3.8 5 5 6.2 6.3 6.8 L7.2 5.7 L9.5 6.4 L9.5 8 C9.5 9 8.8 9.5 8 9.5 C4 9.2 0.8 6 0.5 2 C0.5 1.2 1 0.5 2 0.5 Z"/></svg>
      </li>
      <li>helpline@bhsanctum.org
        <svg viewBox="0 0 10 10"><path d="M0.5 2 L9.5 2 L9.5 8.5 L0.5 8.5 Z M1.2 2.6 L5 5.6 L8.8 2.6" stroke="#1f58a3" stroke-width="0.8"/></svg>
      </li>
      <li>www.bhsanctum.org
        <svg viewBox="0 0 10 10"><circle cx="5" cy="5" r="4.5"/></svg>
      </li>
    </ul>
  </section>

  <section class="card card-back" aria-label="Card back">
    <div class="brand">
      <span class="brand-mark"></span>
      <span class="brand-name">Briarwood Heron<br>Sanctuary</span>
    </div>
  </section>
</body>
</html>
```